KerrLow Farm

Need a nice simple clean double sided business card that has our logo and info on:
Kerr Low Farm
Martin & Felicity Kerr Low
kerrlowfarm@mailbarn.example
Martin: 1-780-555-0148
Felicity: 1-780-555-0193
Instagram @ kerrlow_farm

Contact Information for Business Card

Martin & Felicity Kerr Low kerrlowfarm@mailbarn.example Martin: 1-780-555-0148 Felicity: 1-780-555-0193

```html
<!DOCTYPE html>
<html lang="en">
<head>
<meta charset="utf-8">
<title>Kerr Low Farm — Business Card</title>
<link rel="stylesheet" href="https://fonts.googleapis.com/css2?family=Open+Sans:wght@400;600;700&display=swap">
<style>
  :root {
    --paper: #ffffff;
    --ink: #1f1f1f;
    --farm-green: #5e9c1c;
    --divider-green: #b9d49a;
    --wheat-gold: rgba(247, 210, 140, 0.55);
    --wheat-leaf: rgba(200, 222, 176, 0.45);
  }
  * { margin: 0; padding: 0; box-sizing: border-box; }
  html, body {
    width: 1200px;
    height: 686px;
    overflow: hidden;
    background: var(--paper);
  }
  .card {
    position: relative;
    width: 1200px;
    height: 686px;
    background: var(--paper);
    font-family: "Open Sans", Arial, sans-serif;
    color: var(--ink);
    overflow: hidden;
  }
  .wheat-backdrop {
    position: absolute;
    left: 860px;
    top: 150px;
    width: 340px;
    height: 536px;
    background:
      radial-gradient(ellipse 38% 42% at 55% 38%, var(--wheat-gold) 0%, rgba(247,210,140,0.18) 60%, rgba(255,255,255,0) 100%),
      radial-gradient(ellipse 45% 35% at 50% 95%, var(--wheat-leaf) 0%, rgba(255,255,255,0) 100%);
  }
  .owners {
    position: absolute;
    right: 51px;
    top: 38px;
    text-align: right;
    line-height: 1.2;
  }
  .owners__names {
    font-size: 26px;
    letter-spacing: 1.5px;
    text-transform: uppercase;
  }
  .owners__surname {
    font-size: 21px;
  }
  .brand {
    position: absolute;
    left: 60px;
    top: 290px;
    width: 460px;
    text-align: center;
  }
  .brand__name {
    font-size: 44px;
    font-weight: 600;
    color: var(--ink);
    letter-spacing: 0.5px;
    white-space: nowrap;
  }
  .divider {
    position: absolute;
    left: 567px;
    top: 130px;
    width: 5px;
    height: 450px;
    background: linear-gradient(to bottom, rgba(185,212,154,0) 0%, var(--divider-green) 50%, rgba(185,212,154,0) 100%);
  }
  .contact {
    position: absolute;
    left: 656px;
    top: 310px;
    list-style: none;
  }
  .contact__item {
    display: flex;
    align-items: center;
    height: 47px;
    font-size: 27px;
  }
  .contact__icon {
    width: 34px;
    height: 24px;
    margin-right: 24px;
    flex: none;
  }
  .contact__label { font-weight: 700; margin-right: 8px; }
</style>
</head>
<body>
  <div class="card">
    <div class="wheat-backdrop" role="img" aria-label="Faint wheat stalks illustration"></div>

    <div class="owners">
      <div class="owners__names">Martin &amp; Felicity</div>
      <div class="owners__surname">Kerr Low</div>
    </div>

    <div class="brand">
      <div class="brand__name">Kerr Low Farm</div>
    </div>

    <div class="divider"></div>

    <ul class="contact">
      <li class="contact__item">
        <svg class="contact__icon" viewBox="0 0 34 24" aria-hidden="true">
          <rect x="1" y="2" width="32" height="20" fill="var(--ink)"/>
          <path d="M1 2 L17 14 L33 2" fill="none" stroke="var(--paper)" stroke-width="2"/>
          <path d="M1 22 L13 11 M33 22 L21 11" stroke="var(--paper)" stroke-width="1.5"/>
        </svg>
        <span>kerrlowfarm@mailbarn.example</span>
      </li>
      <li class="contact__item">
        <svg class="contact__icon" viewBox="0 0 34 24" aria-hidden="true">
          <path d="M2 8 Q17 -2 32 8 L29 11 L24 9 L24 6 Q17 4 10 6 L10 9 L5 11 Z" fill="var(--ink)"/>
          <path d="M9 11 L25 11 L30 22 L4 22 Z" fill="var(--ink)"/>
          <circle cx="17" cy="16" r="3" fill="var(--paper)"/>
        </svg>
        <span class="contact__label">Martin:</span><span>1-780-555-0148</span>
      </li>
      <li class="contact__item">
        <svg class="contact__icon" viewBox="0 0 34 24" aria-hidden="true">
          <path d="M2 8 Q17 -2 32 8 L29 11 L24 9 L24 6 Q17 4 10 6 L10 9 L5 11 Z" fill="var(--ink)"/>
          <path d="M9 11 L25 11 L30 22 L4 22 Z" fill="var(--ink)"/>
          <circle cx="17" cy="16" r="3" fill="var(--paper)"/>
        </svg>
        <span class="contact__label">Felicity:</span><span>1-780-555-0193</span>
      </li>
    </ul>
  </div>
</body>
</html>
```